Bed Company needs business card

Hello, we are a bed company that makes specialized magnets for beds. We are an alternative healing company. I need a modern and upscale business card. Please incorporate my logo for the card.

Accepted file formats are AI, EPS, and Press-Ready PDFS.

Please include all fonts or convert them to outlines regardless of file type.

If you are designing the card in Photoshop the file Must be 1200dpi.

I am open to anything for the business card.  I really like all of your designs and if you want to change the color of the logo, you can.  I will be making the final selection by Friday.  Thank You for all of your designs.  Feel Free to submit different color logos if you want.  

Reason: I will make a decision Final on Friday April 20th. 2012. Good Luck and Thank you all for the designs.

Target Market(s)

My target Market is people, who are looking for alternative healing.

Industry/Entity Type

Business

Requirements
Must have
• My logo must be incorporated. The front card must have

Name
Job Title

Address
Work
Cell
Fax
email
web

Just put in fake info for the card.

The back of the card. I want the logo on the back with color. I just want it to look modern and cool.

```html
<!DOCTYPE html>
<html lang="en">
<head>
<meta charset="utf-8">
<title>Restwell Coil – Business Card</title>
<link rel="stylesheet" href="https://fonts.googleapis.com/css2?family=Cinzel:wght@400;500&family=Open+Sans:wght@400&display=swap">
<style>
  :root {
    --lime: #4cff00;
    --forest: #167400;
    --paper: #ffffff;
  }
  * { margin: 0; padding: 0; box-sizing: border-box; }
  html, body {
    width: 1200px;
    height: 754px;
    overflow: hidden;
    background: var(--paper);
  }
  .card {
    position: relative;
    width: 1200px;
    height: 754px;
    background: var(--paper);
    font-family: "Open Sans", "Segoe UI", sans-serif;
    color: var(--paper);
    overflow: hidden;
  }
  .block { position: absolute; background: var(--lime); }
  .block--top-left     { left: 0;     top: 0;     width: 491px; height: 132px; }
  .block--top-right    { left: 686px; top: 0;     width: 514px; height: 132px; }
  .block--bottom-left  { left: 0;     top: 330px; width: 491px; height: 424px; }
  .block--bottom-right { left: 686px; top: 330px; width: 514px; height: 424px; }

  .band { position: absolute; background: var(--forest); }
  .band--horizontal { left: 0; top: 142px; width: 1200px; height: 177px; }
  .band--vertical   { left: 502px; top: 0; width: 177px; height: 754px; }

  .identity {
    position: absolute;
    left: 0;
    top: 176px;
    width: 1200px;
    text-align: center;
  }
  .identity__name {
    font-family: "Cinzel", "Times New Roman", serif;
    font-weight: 400;
    font-size: 64px;
    line-height: 1;
    letter-spacing: 2px;
    color: var(--forest);
    -webkit-text-stroke: 1.3px var(--paper);
  }
  .identity__name .initial { font-size: 78px; }
  .identity__title {
    margin-top: 8px;
    font-size: 35px;
    line-height: 1.2;
    color: var(--paper);
  }

  .contact {
    position: absolute;
    left: 64px;
    top: 407px;
    font-size: 28px;
    line-height: 41.5px;
  }
  .contact__row { display: flex; }
  .contact__label { width: 80px; }
  .contact__colon { width: 41px; }
  .contact__online { margin-top: 38px; }
  .contact__web { color: var(--forest); }

  .event {
    position: absolute;
    left: 748px;
    top: 407px;
    font-size: 28px;
    line-height: 41.5px;
  }
  .event__company { margin-bottom: 41.5px; }
</style>
</head>
<body>
  <div class="card">
    <div class="block block--top-left"></div>
    <div class="block block--top-right"></div>
    <div class="block block--bottom-left"></div>
    <div class="block block--bottom-right"></div>
    <div class="band band--horizontal"></div>
    <div class="band band--vertical"></div>

    <div class="identity">
      <h1 class="identity__name"><span class="initial">D</span>ANIEL <span class="initial">H</span>ARROW</h1>
      <p class="identity__title">director</p>
    </div>

    <div class="contact">
      <div class="contact__row"><span class="contact__label">tel</span><span class="contact__colon">:</span><span>(555) 214 387</span></div>
      <div class="contact__row"><span class="contact__label">cell</span><span class="contact__colon">:</span><span>(555) 214 390</span></div>
      <div class="contact__row"><span class="contact__label">fax</span><span class="contact__colon">:</span><span>(555) 306 112</span></div>
      <div class="contact__online">
        <div class="contact__email">office@restwellcoil.com</div>
        <div class="contact__web">www.restwell-coil.com</div>
      </div>
    </div>

    <div class="event">
      <div class="event__company">Restwell Coil, Ltd</div>
      <div>July 9-12, 2013,</div>
      <div>Lakeshore Hall East,</div>
      <div>Northport IL, Booth 2208</div>
    </div>
  </div>
</body>
</html>
```